People/Expertise finder to associate people to experts, services and products

Design a mock-up for a Kinward Atlas/expertise finder system. The people/expertise finder project is targeting to relate people to experts, countries and core operations. We are expecting the final UI to be responsive. The styleguide that is followed in the enterprise is attached for reference. further documents outlining the vision is also attached. Based on queries kindly use the tovel net profile as an example of profile page. People will search using the enterprise search on names, skills etc to find matching people.

Kinward Atlas

3 page

• The UI should be aesthetically good and should bring in the industry standards

```html
<!DOCTYPE html>
<html lang="en">
<head>
<meta charset="utf-8">
<title>Kinward Atlas – Profile</title>
<link href="https://fonts.googleapis.com/css2?family=Roboto:wght@400;500;700&display=swap" rel="stylesheet">
<style>
:root{
  --blue:#0a8fd1;
  --green:#7cc24e;
  --dark:#2b2b2b;
  --page:#f4f4f4;
  --white:#ffffff;
  --text:#222222;
  --muted:#666666;
  --bar:#ebebeb;
  --bar-dark:#e0e0e0;
  --grey-btn:#9a9a9a;
}
*{box-sizing:border-box;margin:0;padding:0}
html,body{width:1200px;height:780px;overflow:hidden}
body{background:var(--page);font-family:'Roboto',Arial,sans-serif;color:var(--text);position:relative}
.abs{position:absolute}
.topbar{left:0;top:0;width:1200px;height:56px;background:linear-gradient(100deg,#0a86cf 0%,#1a9bd0 35%,#3aa9a0 60%,#6dbf58 85%,#8acb5a 100%);color:var(--white)}
.brand{left:252px;top:8px;display:flex;align-items:center;gap:6px;font-size:11px;font-weight:500}
.brand-dot{width:40px;height:40px;border-radius:50%;background:var(--white)}
.account{left:312px;top:20px;font-size:12px;display:flex;gap:8px;align-items:center}
.user{left:776px;top:20px;font-size:12px;display:flex;gap:14px;align-items:center}
.navbar{left:0;top:56px;width:1200px;height:47px;background:var(--dark)}
.nav-links{left:252px;top:17px;display:flex;gap:22px;color:var(--white);font-size:12px}
.scope{left:590px;top:9px;width:72px;height:28px;background:var(--grey-btn);color:var(--white);font-size:12px;border-radius:2px;display:flex;align-items:center;justify-content:center;gap:4px}
.search{left:667px;top:9px;width:227px;height:28px;background:var(--white);font-size:12px;color:#aaa;padding:8px 9px;border-radius:2px}
.advanced{left:901px;top:17px;color:var(--white);font-size:12px}
.welcome{left:250px;top:118px;font-size:11.5px;color:#555}
.tools{left:656px;top:118px;display:flex;gap:7px}
.card{background:var(--white)}
.photo{background:linear-gradient(135deg,#d8d4cc 0%,#8a6a58 50%,#7a2a30 100%)}
.name{left:428px;top:155px;font-size:19px;font-weight:500}
.tag{font-size:9px;color:#444}
.row-label{font-size:8.5px;color:#777}
.row-text{font-size:8px;color:#222;line-height:10px}
.btn-primary{background:var(--blue);color:var(--white);font-size:9px;font-weight:500;display:flex;align-items:center;justify-content:center}
.btn-edit{background:var(--grey-btn);color:var(--white);font-size:9px;display:flex;align-items:center;justify-content:center}
.link-bar{left:249px;top:338px;width:469px;height:34px;background:var(--bar)}
.contact{left:618px;top:338px;width:100px;height:34px;background:var(--bar-dark);font-size:10px;font-weight:500;color:#444;display:flex;align-items:center;justify-content:center;gap:6px}
.tab{left:249px;top:380px;width:97px;height:26px;background:var(--dark);color:var(--white);font-size:11px;display:flex;align-items:center;justify-content:center}
.update{left:249px;top:416px;width:434px;height:28px;border:1px solid #ccc;background:var(--white);font-size:8px;color:#999;padding:9px 7px;border-radius:2px}
.side-title{font-size:10.5px;font-weight:500}
.thumb{width:40px;height:34px}
.suggest{background:#e4e4e4}
.follow-btn{left:800px;top:446px;width:80px;height:29px;background:var(--blue);color:var(--white);font-size:9.5px;font-weight:500;display:flex;align-items:center;justify-content:center}
.center{text-align:center}
</style>
</head>
<body>
<header class="abs topbar">
  <div class="abs brand"><span class="brand-dot"></span></div>
  <div class="abs" style="left:252px;top:46px;font-size:0"></div>
  <div class="abs account">
    <span>Account type : &nbsp;Basic</span>
    <svg width="11" height="9" viewBox="0 0 11 9"><rect width="11" height="9" rx="1" fill="#fff"/><path d="M0 1l5.5 4L11 1" stroke="#1a9bd0" fill="none"/></svg>
    <span>7</span>
    <svg width="10" height="10" viewBox="0 0 10 10"><path d="M1 0v10M1 1h8l-2 2.5L9 6H1" fill="#fff" stroke="#fff"/></svg>
  </div>
  <div class="abs user"><span>Odell Prane ▾</span><span>Add Connections</span></div>
</header>
<div class="abs" style="left:296px;top:44px"></div>

<nav class="abs navbar">
  <div class="abs nav-links"><span>Home</span><span>Profile</span><span>Groups</span><span>Jobs</span><span>News</span><span>More</span></div>
  <div class="abs scope">People <span style="font-size:8px">▼</span></div>
  <div class="abs search">Search</div>
  <div class="abs advanced">Advanced</div>
</nav>

<p class="abs welcome">Welcome to the new profile have you updated yours?</p>
<div class="abs tools">
  <svg width="11" height="9" viewBox="0 0 11 9"><rect width="11" height="9" rx="1" fill="#555"/><path d="M0 1l5.5 4L11 1" stroke="#f4f4f4" fill="none"/></svg>
  <svg width="10" height="10" viewBox="0 0 10 10"><circle cx="8" cy="2" r="1.8" fill="#555"/><circle cx="2" cy="5" r="1.8" fill="#555"/><circle cx="8" cy="8" r="1.8" fill="#555"/><path d="M8 2L2 5l6 3" stroke="#555"/></svg>
  <span style="font-size:10px;font-weight:700;color:#555;line-height:10px">?</span>
  <svg width="10" height="10" viewBox="0 0 10 10"><rect x="2" y="0" width="6" height="3" fill="#555"/><rect x="0" y="3" width="10" height="4" fill="#555"/><rect x="2" y="6" width="6" height="4" fill="none" stroke="#555"/></svg>
</div>

<section class="abs card" style="left:249px;top:145px;width:469px;height:193px"></section>
<div class="abs photo" role="img" aria-label="Portrait photo of the profile owner" style="left:249px;top:157px;width:163px;height:167px"></div>
<h1 class="abs name">Maren Holt</h1>
<p class="abs tag" style="left:428px;top:180px">Design is my lifelong creaft</p>
<p class="abs tag" style="left:428px;top:194px">San franoisco bay area internet</p>
<span class="abs row-label" style="left:426px;top:214px">Previous</span>
<p class="abs row-text" style="left:480px;top:213px;width:220px">Lorem Ipsum is simply dummy text of the printing and typesetting industry.</p>
<span class="abs row-label" style="left:426px;top:248px">Education</span>
<span class="abs row-label" style="left:480px;top:248px;color:#555">Lorem Ipsum is simply dummy</span>
<div class="abs btn-primary" style="left:423px;top:296px;width:126px;height:28px">Improve Your Profile</div>
<div class="abs btn-edit" style="left:554px;top:296px;width:36px;height:28px">Edit</div>
<div class="abs btn-edit" style="left:591px;top:296px;width:18px;height:28px;font-size:7px">▼</div>

<div class="abs link-bar">
  <span class="abs" style="left:8px;top:12px;width:12px;height:12px;background:#555;border-radius:2px"></span>
  <span class="abs" style="left:32px;top:12px;font-size:8px;color:#333">tovel.net/start/?lastWidget=uno_goals_takeover</span>
</div>
<div class="abs contact">
  <svg width="10" height="10" viewBox="0 0 10 10"><rect x="0" y="1" width="10" height="9" fill="none" stroke="#777"/><path d="M0 3.5h10M3 1v8M7 1v8M0 6.5h10" stroke="#777" stroke-width=".7"/></svg>
  Contact info
</div>

<div class="abs card" style="left:346px;top:380px;width:372px;height:26px"></div>
<div class="abs tab">Activty</div>
<div class="abs update">Share an update.....</div>
<div class="abs card" style="left:249px;top:454px;width:469px;height:113px"></div>

<aside class="abs card" style="left:726px;top:145px;width:224px;height:369px"></aside>
<h2 class="abs side-title" style="left:740px;top:155px">People you may know</h2>
<div class="abs" style="left:740px;top:178px;display:flex;gap:1px">
  <div class="thumb" role="img" aria-label="Suggested contact photo" style="background:linear-gradient(135deg,#c79a5e,#6a4e3a)"></div>
  <div class="thumb" role="img" aria-label="Suggested contact photo" style="background:linear-gradient(135deg,#b8613a,#5e3a2a)"></div>
  <div class="thumb" role="img" aria-label="Suggested contact photo" style="background:linear-gradient(135deg,#d8dde2,#4a6a8a)"></div>
  <div class="thumb" role="img" aria-label="Suggested contact photo" style="background:linear-gradient(135deg,#3a3430,#a89a8a)"></div>
  <div class="thumb" role="img" aria-label="Suggested contact photo" style="background:linear-gradient(135deg,#5a5048,#2a2e38)"></div>
</div>
<h3 class="abs" style="left:740px;top:220px;font-size:11px;font-weight:500">Talia Voss</h3>
<p class="abs" style="left:741px;top:235px;width:200px;font-size:8.5px;line-height:11px">Lorem Ipsum is simply dummy text of the printing and typesetting industry.</p>
<div class="abs" style="left:741px;top:268px;width:198px;height:1px;background:#ddd"></div>

<div class="abs suggest" style="left:735px;top:280px;width:209px;height:126px"></div>
<p class="abs center" style="left:735px;top:292px;width:209px;font-size:8px;font-weight:500">Grow Your Career By Following</p>
<p class="abs center" style="left:735px;top:303px;width:209px;font-size:10.5px;font-weight:500">Harbor Crest Limited</p>
<div class="abs" role="img" aria-label="Your profile photo" style="left:749px;top:327px;width:52px;height:42px;background:linear-gradient(135deg,#d8d4cc,#8a6a58 55%,#7a2a30)"></div>
<div class="abs" role="img" aria-label="Company cover photo" style="left:860px;top:327px;width:52px;height:42px;background:linear-gradient(135deg,#a07a58,#5a3a2a)"></div>
<p class="abs center" style="left:745px;top:376px;width:60px;font-size:10px;color:#777">You</p>
<p class="abs center" style="left:840px;top:375px;width:92px;font-size:9.5px;color:#777;line-height:10px">Harbor Crest Limited</p>
<p class="abs center" style="left:740px;top:414px;width:200px;font-size:9px;color:#666;line-height:11px">Lorem Ipsum is simply dummy text of the printing and typesetting industry.</p>
<div class="abs follow-btn">Follow</div>
</body>
</html>
```